New Business Cards for Organic Meat Farm

We need a business card designed for Thornbury Farm, a meat farm in western MA. Our logo uses a hand-drawn woodcut (attached). Our color palette has been simply black and white (shown in notepad and picture of our food truck). While we are based out of western MA, we have ambitions to grow nationally, so our hope is for a classy and memorable card which will be printed on a premium quality stock from a printer like printkestrel.com.
Target Market(s)
consumers of quality meats, restauranteurs, partnering farms
Industry/Entity Type
Farming and prepared meat products
Contact Information for Business Card
Wendell Pruitt, President/Owner, wendell@thornburyfarm.com, mobile: 413-555-0172, phone: 413-555-0148, thornburyfarm.com, facebook: @thornburyfarm, instagram: @thornburyfarmma
Colors
Designer to choose colors to be used in the design.
Look and feel

```html
<!DOCTYPE html>
<html lang="en">
<head>
<meta charset="utf-8">
<title>Thornbury Farm – Business Card</title>
<link href="https://fonts.googleapis.com/css2?family=Playfair+Display:ital,wght@0,400;0,700;0,900;1,400&family=EB+Garamond:ital,wght@0,400;1,400&display=swap" rel="stylesheet">
<style>
  :root {
    --backdrop: #2b2b2b;
    --card: #1c1c1c;
    --card-edge: #262626;
    --illustration-a: #2a2a2a;
    --illustration-b: #202020;
    --foil: #b9b9b9;
    --white: #f4f4f4;
    --text: #d6d6d6;
    --accent: #c98a4b;
  }
  * { margin: 0; padding: 0; box-sizing: border-box; }
  html, body { width: 1200px; height: 875px; overflow: hidden; }
  body {
    background: var(--backdrop);
    display: flex;
    align-items: center;
    justify-content: center;
    gap: 40px;
  }
  .card {
    position: relative;
    width: 540px;
    height: 309px;
    border-radius: 18px;
    background: var(--card);
    box-shadow: 0 18px 40px rgba(0,0,0,.45);
    overflow: hidden;
  }

  /* Front */
  .card-front {
    display: flex;
    flex-direction: column;
    align-items: center;
    justify-content: center;
    gap: 10px;
  }
  .brand-name {
    font-family: "Playfair Display", serif;
    font-weight: 700;
    font-size: 42px;
    color: var(--foil);
    letter-spacing: .5px;
  }
  .established {
    font-family: "Playfair Display", serif;
    font-weight: 700;
    font-size: 11px;
    letter-spacing: 4px;
    color: var(--foil);
  }

  /* Back */
  .farmhouse-art {
    position: absolute;
    inset: 0;
    background: radial-gradient(ellipse at 55% 45%, var(--illustration-a) 0%, var(--illustration-b) 75%);
  }
  .card-back .content {
    position: absolute;
    inset: 0;
    display: flex;
    align-items: center;
    padding: 0 30px 0 40px;
  }
  .identity { width: 200px; text-align: right; padding-right: 22px; }
  .person-name {
    font-family: "Playfair Display", serif;
    font-weight: 900;
    font-size: 25px;
    color: var(--white);
    line-height: 1.05;
    text-transform: uppercase;
  }
  .person-title {
    font-family: "Playfair Display", serif;
    font-size: 14px;
    color: var(--accent);
    margin-top: 4px;
  }
  .divider { width: 1.5px; height: 140px; background: var(--white); }
  .contact-list {
    list-style: none;
    padding-left: 20px;
    font-family: "EB Garamond", serif;
    font-size: 14px;
    color: var(--text);
    line-height: 1.35;
  }
  .contact-list li { display: flex; align-items: flex-start; gap: 9px; margin-bottom: 4px; }
  .contact-list svg { width: 12px; height: 12px; margin-top: 3px; flex: none; fill: var(--accent); }
  .social {
    position: absolute;
    left: 262px;
    bottom: 26px;
    display: flex;
    align-items: center;
    gap: 8px;
    font-family: "EB Garamond", serif;
    font-style: italic;
    font-size: 15px;
    color: var(--text);
  }
  .social .dot { width: 11px; height: 11px; border-radius: 50%; background: var(--accent); }
</style>
</head>
<body>

  <section class="card card-front" aria-label="Card front">
    <div class="brand-name">Thornbury Farm</div>
    <div class="established">EST. 1899</div>
  </section>

  <section class="card card-back" aria-label="Card back">
    <div class="farmhouse-art" role="img" aria-label="Faint woodcut illustration of the farmhouse and trees"></div>
    <div class="content">
      <div class="identity">
        <div class="person-name">Wendell Pruitt</div>
        <div class="person-title">President/Owner</div>
      </div>
      <div class="divider"></div>
      <ul class="contact-list">
        <li>
          <svg viewBox="0 0 12 12"><path d="M6 0a4 4 0 0 0-4 4c0 3 4 8 4 8s4-5 4-8a4 4 0 0 0-4-4zm0 5.6A1.6 1.6 0 1 1 6 2.4a1.6 1.6 0 0 1 0 3.2z"/></svg>
          <span>48 Orchard Hill Rd<br>Easton Ridge, MA 01299</span>
        </li>
        <li>
          <svg viewBox="0 0 12 12"><path d="M2.5 0.5l2 2.2-1 1.4c.7 1.6 1.9 2.8 3.4 3.4l1.4-1 2.2 2-1.3 2.5C4.8 10.5 1.5 7.2 0 2z"/></svg>
          <span>413-555-0148</span>
        </li>
        <li>
          <svg viewBox="0 0 12 12"><path d="M3 0h6a1 1 0 0 1 1 1v10a1 1 0 0 1-1 1H3a1 1 0 0 1-1-1V1a1 1 0 0 1 1-1zm.5 1.5v8h5v-8zM6 10.2a.6.6 0 1 0 0 1.2.6.6 0 0 0 0-1.2z"/></svg>
          <span>413-555-0172</span>
        </li>
        <li>
          <svg viewBox="0 0 12 12"><path d="M0 2h12v8H0zm1 1v.3l5 3.3 5-3.3V3zm0 1.5V9h10V4.5L6 7.8z"/></svg>
          <span>wendell@thornburyfarm.com</span>
        </li>
        <li>
          <svg viewBox="0 0 12 12"><path d="M6 0a6 6 0 1 0 0 12A6 6 0 0 0 6 0zm0 1c.7 0 1.5 1.6 1.7 4.5H4.3C4.5 2.6 5.3 1 6 1zM1 6.5h2.3c.1 1.6.4 3 .9 3.9A5 5 0 0 1 1 6.5zm0-1A5 5 0 0 1 4.2 1.6c-.5.9-.8 2.3-.9 3.9zm5 5.5c-.7 0-1.5-1.6-1.7-4.5h3.4C7.5 9.4 6.7 11 6 11zm1.8-.6c.5-.9.8-2.3.9-3.9H11a5 5 0 0 1-3.2 3.9zm.9-4.9c-.1-1.6-.4-3-.9-3.9A5 5 0 0 1 11 5.5z"/></svg>
          <span>thornburyfarm.com</span>
        </li>
      </ul>
    </div>
    <div class="social">
      <span class="dot"></span>
      <span>@thornburyfarm</span>
    </div>
  </section>

</body>
</html>
```